Business card design needed

We are an electrical Contracting Company with a solar power division and Air conditioning
Our primary business is Solar PV, Solar Hot water, Electrical Maintenance, Repairs, and installs. Air Conditioning Installation is also one of our areas,
My Web Site is: www.tpkvolta.com
and www.dorianwhitlockelectrical.com.au.
If we could incorporate the back feature photos on the tpkvolta website that would help resemble our vehicles help the customers remember us.

Cheers
Dorian
0427361985

Industry/Entity Type

Electrical

Contact Information for Business Card

tpkvolta.com electrical contractors
a division of Dorian Whitlock Electrical P/L
22/9 Pellow Crescent
Corvan Point Q 4395
Phone: 0427361985
Office: 0743827519
Fax: 0743827604
email: dwtelectrical@fernpost.com
Website: www.tpkvolta.com
www.dorianwhitlockelectrical.com.au
License number: Q31952,RVP A2758164, NSW 31692K,MTV L084217

```html
<!DOCTYPE html>
<html lang="en">
<head>
<meta charset="utf-8">
<title>TPK Volta business card concepts</title>
<link href="https://fonts.googleapis.com/css2?family=Arimo:wght@400;700&display=swap" rel="stylesheet">
<style>
:root{
  --sheet:#ececec;
  --sheet-edge:#f7f7f7;
  --orange:#ee6a21;
  --ink:#2b2b2b;
  --grey-logo:#8c8c8c;
  --white:#ffffff;
  --sky:#dcedf9;
  --meadow:#5f7f24;
  --meadow-light:#a9c47c;
}
*{margin:0;padding:0;box-sizing:border-box}
html,body{width:1200px;height:797px;overflow:hidden}
body{background:linear-gradient(90deg,var(--sheet-edge) 0 15px,var(--sheet) 15px);font-family:"Arimo",Arial,sans-serif;color:var(--ink);position:relative}
.side-label{position:absolute;top:18px;font-size:21px;color:#333}
.row-number{position:absolute;font-size:17px;color:#333}
.card{position:absolute;width:532px;height:306px;border-radius:18px;overflow:hidden;box-shadow:0 2px 8px rgba(0,0,0,.25),0 0 0 1px rgba(255,255,255,.8)}
.abs{position:absolute}
.sky-panel{background:linear-gradient(180deg,var(--sky) 0%,#eef5f4 48%,#c9d9a4 58%,var(--meadow-light) 66%,var(--meadow) 100%)}
.photo-daisy{background:
  linear-gradient(90deg,rgba(255,255,255,0) 0%,rgba(255,255,255,.25) 45%,rgba(255,255,255,0) 100%),
  linear-gradient(180deg,#e4eff7 0%,#eef2ec 28%,#e4eadb 50%,#b9cc8a 70%,#7d9c42 86%,#58782a 100%)}
.photo-meadow{background:
  linear-gradient(90deg,rgba(255,255,255,.15) 0%,rgba(255,255,255,0) 40%,rgba(255,255,255,.3) 80%,rgba(255,255,255,.15) 100%),
  linear-gradient(180deg,#f4f8fb 0%,#e9efe0 30%,#cddcaa 55%,#9bb55f 78%,#5f7e28 100%)}
.accent-bar{background:var(--orange);width:6px;top:0;height:100%}
.brand-name{font-weight:700;color:var(--grey-logo);font-size:31px;letter-spacing:-1px;line-height:1;display:flex;align-items:flex-end;gap:4px}
.brand-name .mark{width:7px;height:7px;background:var(--orange);display:inline-block;margin-bottom:4px}
.headline{font-weight:700;color:var(--orange);font-size:20.5px;white-space:nowrap}
.headline.outlined{text-shadow:-1px -1px 0 #fff,1px -1px 0 #fff,-1px 1px 0 #fff,1px 1px 0 #fff,0 2px 3px rgba(0,0,0,.35)}
.division{font-weight:700;font-size:12px;white-space:nowrap}
.division.light{color:var(--white);font-size:11.5px;text-shadow:0 0 2px rgba(0,0,0,.7)}
.web{font-weight:700;color:var(--white);font-size:15px;white-space:nowrap}
.tagline{font-size:11px;color:#222}
.back-heading{font-weight:700;color:var(--orange);font-size:12.5px;line-height:17px;white-space:nowrap;letter-spacing:.1px}
.address{font-size:14px}
.contact-list{list-style:none;font-size:14px;line-height:21px}
.contact-list li{display:flex;align-items:flex-start;gap:8px;white-space:nowrap}
.contact-list svg{width:14px;height:14px;margin-top:3px;flex:none;stroke:#333;fill:none;stroke-width:1.3}
.license{font-size:12px;line-height:19px;color:var(--white);white-space:nowrap}
.license.dark{color:#444;font-size:11.5px}
.frost-panel{background:rgba(255,255,255,.55);border-radius:12px}
</style>
</head>
<body>
<div class="side-label" style="left:249px">Front side</div>
<div class="side-label" style="left:853px">Back side</div>
<div class="row-number" style="left:23px;top:62px">1</div>
<div class="row-number" style="left:0;top:438px">2</div>

<!-- Option 1 front -->
<section class="card" style="left:65px;top:55px">
  <div class="abs sky-panel" style="left:0;top:0;width:343px;height:100%"></div>
  <div class="abs accent-bar" style="left:343px"></div>
  <div class="abs photo-daisy" role="img" aria-label="Close-up photo of a white daisy in a green meadow" style="left:349px;top:0;width:183px;height:100%"></div>
  <div class="abs brand-name" style="left:99px;top:60px">tpkvolta.com<span class="mark"></span></div>
  <div class="abs headline" style="left:22px;top:124px">ELECTRICAL CONTRACTORS</div>
  <div class="abs division" style="left:22px;top:161px">A DIVISION OF DORIAN WHITLOCK ELECTRICAL</div>
  <div class="abs web" style="left:22px;top:232px">www.dorianwhitlockelectrical.com.au</div>
</section>

<!-- Option 1 back -->
<section class="card" style="left:635px;top:55px">
  <div class="abs photo-daisy" role="img" aria-label="Close-up photo of a white daisy in a green meadow" style="left:0;top:0;width:183px;height:100%"></div>
  <div class="abs accent-bar" style="left:183px"></div>
  <div class="abs sky-panel" style="left:189px;top:0;width:343px;height:100%"></div>
  <div class="abs back-heading" style="left:208px;top:37px">TPKVOLTA.COM&nbsp; ELECTRICAL&nbsp; CONTRACTORS<br>A DIVISION OF DORIAN WHITLOCK ELECTRICAL</div>
  <div class="abs address" style="left:208px;top:86px">P/L 22/9 Pellow Crescent Corvan Point Q 4395</div>
  <ul class="abs contact-list" style="left:210px;top:119px">
    <li><svg viewBox="0 0 14 14"><rect x="3.5" y="1" width="7" height="12" rx="1"/></svg>0427361985</li>
    <li><svg viewBox="0 0 14 14"><path d="M3 1.5l2 2-1 2c1 2 2.5 3.5 4.5 4.5l2-1 2 2-1.5 1.5C6 12 2 8 1.5 3z" fill="#333"/></svg>0743827519</li>
    <li><svg viewBox="0 0 14 14"><rect x="4" y="1.5" width="6" height="4"/><rect x="1.5" y="5.5" width="11" height="6"/><path d="M4 9h6"/></svg>0743827604</li>
    <li><svg viewBox="0 0 14 14"><rect x="1" y="3" width="12" height="8"/><path d="M1 3l6 5 6-5"/></svg>dwtelectrical@fernpost.com</li>
    <li><svg viewBox="0 0 14 14" style="margin-top:12px"><circle cx="7" cy="7" r="5.5"/><ellipse cx="7" cy="7" rx="2.5" ry="5.5"/><path d="M1.5 7h11"/></svg><span>www.tpkvolta.com<br>www.dorianwhitlockelectrical.com.au</span></li>
  </ul>
  <div class="abs license" style="left:208px;top:258px">License number:<br>Q31952,RVP A2758164, NSW 31692K,MTV L084217</div>
</section>

<!-- Option 2 front -->
<section class="card" style="left:65px;top:447px">
  <div class="abs photo-meadow" role="img" aria-label="Photo of a sunlit meadow with a large white daisy on the right" style="inset:0"></div>
  <div class="abs tagline" style="left:100px;top:39px">Gold Coast Solar Panels!</div>
  <div class="abs brand-name" style="left:99px;top:68px">tpkvolta.com<span class="mark"></span></div>
  <div class="abs headline outlined" style="left:29px;top:145px">ELECTRICAL CONTRACTORS</div>
  <div class="abs division light" style="left:29px;top:185px">A DIVISION OF DORIAN WHITLOCK ELECTRICAL</div>
  <div class="abs web" style="left:95px;top:244px;font-size:16px">www.tpkvolta.com</div>
</section>

<!-- Option 2 back -->
<section class="card" style="left:633px;top:447px">
  <div class="abs photo-meadow" role="img" aria-label="Photo of a sunlit meadow with a large white daisy on the left" style="inset:0"></div>
  <div class="abs frost-panel" style="left:162px;top:71px;width:348px;height:214px"></div>
  <ul class="abs contact-list" style="left:179px;top:79px">
    <li><svg viewBox="0 0 14 14"><rect x="3.5" y="1" width="7" height="12" rx="1"/></svg>0427361985</li>
    <li><svg viewBox="0 0 14 14"><path d="M3 1.5l2 2-1 2c1 2 2.5 3.5 4.5 4.5l2-1 2 2-1.5 1.5C6 12 2 8 1.5 3z" fill="#333"/></svg>0743827519</li>
    <li><svg viewBox="0 0 14 14"><rect x="4" y="1.5" width="6" height="4"/><rect x="1.5" y="5.5" width="11" height="6"/><path d="M4 9h6"/></svg>0743827604</li>
    <li><svg viewBox="0 0 14 14"><rect x="1" y="3" width="12" height="8"/><path d="M1 3l6 5 6-5"/></svg>dwtelectrical@fernpost.com</li>
    <li><svg viewBox="0 0 14 14" style="margin-top:12px"><circle cx="7" cy="7" r="5.5"/><ellipse cx="7" cy="7" rx="2.5" ry="5.5"/><path d="M1.5 7h11"/></svg><span>www.tpkvolta.com<br>www.dorianwhitlockelectrical.com.au</span></li>
    <li style="margin-left:-8px"><svg viewBox="0 0 14 14" style="width:20px"><path d="M7 13s-4.5-4.5-4.5-7.5a4.5 4.5 0 0 1 9 0C11.5 8.5 7 13 7 13z"/><circle cx="7" cy="5.5" r="1.6"/></svg>P/L 22/9 Pellow Crescent Corvan Point Q 4395</li>
  </ul>
  <div class="abs license dark" style="left:187px;top:241px">License number:<br>Q31952,RVP A2758164, NSW 31692K,MTV L084217</div>
</section>
</body>
</html>
```